Lark Stewardship Business Card design

We need a creative business card design for our hospitality management company
We need the following information:
Our business Logo: Lark Stewardship
Name: Mira Dalvorsen
Phone number: 0468 319 542
Email: mira@larkstewardship.com.au
Address: 214/53 Pemberly Street, South Melbourne 3206
Web: www.larkstewardship.com.au
I need the design to be a working file so that I can insert the names and numbers of the other staff members of our business.
The cards need to be 90 x 40mm
Thanks
Hospitality

```html
<!DOCTYPE html>
<html lang="en">
<head>
<meta charset="utf-8">
<title>Lark Stewardship Business Card</title>
<link rel="stylesheet" href="https://fonts.googleapis.com/css2?family=Oswald:wght@600&family=Open+Sans:wght@400;600&display=swap">
<style>
  :root {
    --navy: #1f477a;
    --navy-deep: #173a66;
    --navy-light: #2c5d95;
    --sky: #2a9fe0;
    --ink: #2b2f36;
    --paper: #ffffff;
    --backdrop: #e9eaec;
  }
  * { box-sizing: border-box; margin: 0; padding: 0; }
  html, body { width: 1200px; height: 951px; overflow: hidden; }
  body {
    background: var(--backdrop);
    position: relative;
    font-family: "Open Sans", sans-serif;
  }
  .card {
    position: absolute;
    width: 700px;
    height: 311px;
    border-radius: 18px;
    overflow: hidden;
  }
  /* Front side */
  .card-front {
    left: 110px;
    top: 90px;
    background: radial-gradient(ellipse at 55% 40%, var(--navy-light) 0%, var(--navy) 55%, var(--navy-deep) 100%);
  }
  .card-front .brand {
    position: absolute;
    left: 0; right: 0;
    top: 110px;
    text-align: center;
    font-family: "Oswald", sans-serif;
    font-weight: 600;
    font-size: 50px;
    letter-spacing: 1px;
    color: var(--paper);
    text-transform: uppercase;
  }
  .card-front .web {
    position: absolute;
    left: 0; right: 0;
    top: 208px;
    text-align: center;
    font-size: 20px;
    letter-spacing: 2px;
    color: var(--paper);
  }
  /* Back side */
  .card-back {
    left: 390px;
    top: 540px;
    background: var(--paper);
  }
  .card-back .swoosh {
    position: absolute;
    inset: 0;
    width: 100%;
    height: 100%;
  }
  .card-back .brand {
    position: absolute;
    left: 30px;
    top: 52px;
    width: 340px;
    text-align: center;
    font-family: "Oswald", sans-serif;
    font-weight: 600;
    font-size: 30px;
    color: var(--navy);
    text-transform: uppercase;
  }
  .details {
    position: absolute;
    left: 40px;
    top: 160px;
    font-size: 15px;
    line-height: 20px;
    color: var(--ink);
    list-style: none;
  }
  .details li {
    display: flex;
    align-items: flex-start;
    gap: 10px;
    margin-bottom: 10px;
  }
  .details svg { flex: none; margin-top: 3px; }
  .details .url-accent { color: var(--sky); }
  .person {
    position: absolute;
    left: 480px;
    top: 110px;
    width: 200px;
    text-align: center;
    color: var(--paper);
  }
  .person .name { font-size: 21px; font-weight: 400; }
  .person .role { font-size: 14px; margin-top: 2px; }
  .person .phone {
    margin-top: 22px;
    font-size: 16px;
    display: flex;
    justify-content: center;
    align-items: center;
    gap: 8px;
  }
</style>
</head>
<body>

<section class="card card-front" aria-label="Card front">
  <p class="brand">Lark Stewardship</p>
  <p class="web">www.larkstewardship.com.au</p>
</section>

<section class="card card-back" aria-label="Card back">
  <svg class="swoosh" viewBox="0 0 700 311" preserveAspectRatio="none" aria-hidden="true">
    <path d="M388 0 C450 60 462 220 412 311 L700 311 L700 0 Z" fill="var(--navy)"/>
    <path d="M372 0 C438 60 452 220 396 311 L414 311 C466 220 452 60 388 0 Z" fill="var(--sky)"/>
    <path d="M350 0 C410 50 430 130 420 200 C440 120 420 50 372 0 Z" fill="var(--navy-deep)"/>
  </svg>

  <p class="brand">Lark Stewardship</p>

  <ul class="details">
    <li>
      <svg width="14" height="13" viewBox="0 0 14 13" aria-hidden="true"><path d="M7 0 L14 6 L12 6 L12 13 L8.5 13 L8.5 9 L5.5 9 L5.5 13 L2 13 L2 6 L0 6 Z" fill="var(--navy-light)"/></svg>
      <span>214/53 Pemberly Street<br>South Melbourne 3206</span>
    </li>
    <li style="margin-bottom:0">
      <svg width="14" height="11" viewBox="0 0 14 11" aria-hidden="true"><rect width="14" height="11" rx="1.5" fill="var(--navy-light)"/><path d="M1 1.5 L7 6 L13 1.5" stroke="#fff" stroke-width="1.2" fill="none"/></svg>
      <span>mira@larkstewardship.com.au</span>
    </li>
    <li>
      <svg width="14" height="14" viewBox="0 0 14 14" aria-hidden="true"><circle cx="7" cy="7" r="7" fill="var(--sky)"/></svg>
      <span>www.<span class="url-accent">larkstewardship</span>.com.au</span>
    </li>
  </ul>

  <div class="person">
    <p class="name">Mira Dalvorsen</p>
    <p class="role">Manager</p>
    <p class="phone">
      <svg width="14" height="14" viewBox="0 0 14 14" aria-hidden="true"><circle cx="7" cy="7" r="6.2" fill="none" stroke="#fff" stroke-width="1.2"/><path d="M5 3.8 L6.2 5.6 L5.4 6.4 C5.9 7.4 6.6 8.1 7.6 8.6 L8.4 7.8 L10.2 9 L9.4 10.2 C7 10 4 7 3.8 4.6 Z" fill="#fff"/></svg>
      <span>0468 319 542</span>
    </p>
  </div>
</section>

</body>
</html>
```